Business card design needed

My company specialises in carpentry and building services.
Based in Brisbane QLD
We also do:
property maintenance
plastering
painting
tiling
property maintenance

Industry/Entity Type

Carpentry

Contact Information for Business Card

ND Services QLD
Neil 0412555783
Derek 0493721068

```html
<!DOCTYPE html>
<html lang="en">
<head>
<meta charset="utf-8">
<title>ND Services QLD – Business Card</title>
<link href="https://fonts.googleapis.com/css2?family=Arimo:wght@400;700&display=swap" rel="stylesheet">
<style>
  :root {
    --backdrop: #5a4330;
    --card-black: #0d0d0d;
    --kraft: #d8c9a6;
    --kraft-dark: #c4b38d;
    --ink: #1c1a17;
  }
  html, body {
    margin: 0;
    padding: 0;
    width: 1200px;
    height: 1000px;
    overflow: hidden;
    background: var(--backdrop);
    font-family: "Arimo", Arial, sans-serif;
  }
  .canvas {
    position: relative;
    width: 1200px;
    height: 1000px;
  }
  .card {
    position: absolute;
    top: 190px;
    width: 380px;
    height: 620px;
    border-radius: 4px;
    overflow: hidden;
    box-shadow: 0 18px 40px rgba(0,0,0,0.45);
  }
  /* Front */
  .card--front {
    left: 170px;
    background: var(--card-black);
    display: flex;
    flex-direction: column;
    justify-content: center;
    align-items: center;
    text-align: center;
    padding: 0 30px;
    box-sizing: border-box;
  }
  .brand__name {
    margin: 0;
    color: var(--kraft);
    font-weight: 400;
    font-size: 34px;
    line-height: 1.1;
  }
  .tagline {
    margin: 16px 0 0;
    color: var(--kraft);
    font-weight: 400;
    font-size: 19px;
    letter-spacing: 0.3px;
  }
  /* Back */
  .card--back {
    left: 650px;
    background: var(--card-black);
  }
  .contacts {
    height: 290px;
    background: var(--kraft);
    color: var(--ink);
    display: flex;
    flex-direction: column;
    justify-content: center;
    align-items: center;
    text-align: center;
  }
  .contact__name {
    font-size: 19px;
    letter-spacing: 1px;
    text-transform: uppercase;
    line-height: 1;
  }
  .contact__phone {
    font-weight: 700;
    font-size: 48px;
    letter-spacing: -0.5px;
    line-height: 1.05;
    margin-bottom: 8px;
  }
  .services {
    list-style: none;
    margin: 0;
    padding: 26px 0 0 36px;
  }
  .services__item {
    color: var(--kraft);
    font-weight: 700;
    font-size: 34px;
    line-height: 1.02;
    letter-spacing: 0.5px;
  }
  .services__rule {
    margin: 28px 0 0 36px;
    width: 300px;
    height: 4px;
    background: var(--kraft-dark);
  }
</style>
</head>
<body>
  <main class="canvas">
    <section class="card card--front" aria-label="Business card front">
      <h1 class="brand__name">ND Services QLD</h1>
      <p class="tagline">carpentry &amp; building services</p>
    </section>

    <section class="card card--back" aria-label="Business card back">
      <div class="contacts">
        <span class="contact__name">Neil</span>
        <span class="contact__phone">0412555783</span>
        <span class="contact__name">Derek</span>
        <span class="contact__phone">0493721068</span>
      </div>
      <ul class="services">
        <li class="services__item">property</li>
        <li class="services__item">maintenance</li>
        <li class="services__item">plastering</li>
        <li class="services__item">painting</li>
        <li class="services__item">tiling</li>
      </ul>
      <div class="services__rule"></div>
    </section>
  </main>
</body>
</html>
```